Online tuition webpage design needed

Hi,
We are starting up an online tuition website for non- English speakers wishing to take an QUOLT test.

The webpage must include a place for people to enroll online in the course.
The home page must have:
• room for a logo (coming shortly, blue in colour)
• different packages of online tuition and payvora
• tool bar showing different pages
• perhaps a video, small pictures

This is my site currently:-

www.lingvarotutors.example

as you can see, I am not very sure how to create a website … The large logo is what I would like to use, but I project has not been finalized yet. Please note, I don’t like the logo being that large!

Sites that are similar to what I am doing and like the design of are:

http://www.tesmarilearn.example.au/fees

https://www.brovaskill.example/index.php

http://www.pelgrimtutorkaspar.example.uk/index.html

http://www.quorvanexams.example/

One thing I need is a place for student s to enroll, and if possible, I would like to use quillet to create exercises for students.
Currently, my site is using pagecraftr. My preference is to use quillet for online activities. I am not sure if I can use both.
Thanks in advance

Target Market(s)

people wising to take an QUOLT test (English proficiency test)

Industry/Entity Type

Online

Colors
3276b5
0292cd

Requirements
Must have
• a place for enrollment and admin login for students
quillet
video
talqo, friendwall, chirplo logos
Nice to have
• a booking calender
Should not have
• too much clutter. must be clean and professional looking

```html
<!DOCTYPE html>
<html lang="en">
<head>
<meta charset="utf-8">
<title>QUOLT Online Tuition</title>
<link rel="stylesheet" href="https://fonts.googleapis.com/css2?family=Open+Sans:wght@300;400;600;700&family=Roboto+Slab:wght@700&display=swap">
<style>
:root{
  --brand:#3276b5;
  --brand-bright:#0292cd;
  --brand-dark:#1f5e9c;
  --ink:#444;
  --muted:#8a8a8a;
  --grey-btn:#8c8c8c;
  --band:#ececec;
  --footer:#3b3b3b;
  --footer-deep:#2f2f2f;
  --accent-red:#d9453a;
  --orange:#f5a623;
  --orange-dark:#e48a0c;
  --gold:#f7d23e;
}
*{box-sizing:border-box;margin:0;padding:0}
html,body{width:1200px;height:2163px;overflow:hidden}
body{position:relative;background:#fff;font-family:"Open Sans",Arial,sans-serif;color:var(--ink)}

/* header */
.site-header{position:absolute;left:0;top:0;width:1200px;height:150px;background:#fff}
.logo{position:absolute;left:145px;top:28px;display:flex;align-items:flex-start;gap:12px}
.logo-square{width:28px;height:28px;background:var(--brand);margin-top:16px}
.logo-name{font-size:54px;font-weight:600;color:var(--brand);line-height:1}
.logo-sub{position:absolute;left:92px;top:66px;font-size:19px;color:#555;white-space:nowrap}
.top-btn{position:absolute;top:30px;height:38px;background:var(--grey-btn);color:#fff;font-size:13px;font-weight:700;display:flex;align-items:center;justify-content:center;border-radius:2px;box-shadow:0 1px 2px rgba(0,0,0,.3)}
.main-nav{position:absolute;top:101px;left:0;width:1200px;font-size:15px;font-weight:600;color:var(--brand-bright)}
.main-nav a{position:absolute;color:inherit;text-decoration:none;white-space:nowrap}
.main-nav .current{color:var(--brand);border-bottom:2px solid var(--brand);padding-bottom:3px}

/* hero */
.hero{position:absolute;left:0;top:150px;width:1200px;height:457px;background:linear-gradient(180deg,#d7d0c7 0%,#cdbfae 45%,#9c8673 100%)}
.hero-features{position:absolute;left:142px;top:242px;width:476px;height:173px;background:rgba(60,60,60,.85);border-radius:3px;padding:14px 0 0 20px;color:#fff;font-size:11px;text-transform:uppercase}
.hero-features li{list-style:none;height:33px;display:flex;align-items:center;gap:8px}
.hero-features li::before{content:"";width:8px;height:8px;border-radius:50%;background:#fff}
.hero-arrow{position:absolute;top:208px;width:42px;height:42px;border-radius:50%;background:#333}
.hero-dots{position:absolute;left:571px;top:417px;display:flex;gap:6px}
.hero-dots span{width:12px;height:12px;border-radius:50%;background:#bbb}
.hero-dots span:first-child{background:#777}

/* welcome */
.welcome-title{position:absolute;left:0;top:625px;width:1200px;text-align:center;font-size:32px;font-weight:300;color:var(--brand)}
.welcome-text{position:absolute;left:150px;top:673px;width:900px;text-align:center;font-size:18px;font-weight:300;line-height:32px;color:#555}
.intro-card{position:absolute;top:754px;width:205px}
.intro-card .thumb{width:205px;height:110px}
.intro-card h3{margin-top:13px;font-size:13px;font-weight:400;color:var(--brand-bright)}
.intro-card p{margin-top:10px;font-size:11px;line-height:20px;color:var(--muted)}
.btn-more{display:inline-flex;align-items:center;justify-content:center;margin-top:12px;width:92px;height:26px;background:var(--grey-btn);color:#fff;font-size:11px;border-radius:2px}

.calendar{position:absolute;left:826px;top:750px;width:265px;height:212px;background:var(--brand);color:#fff;font-size:9px}
.calendar .close{position:absolute;right:6px;top:2px;font-size:14px;font-weight:700}
.cal-head{position:absolute;left:0;top:26px;width:265px;text-align:center;font-size:9px}
.cal-head .prev{position:absolute;left:28px}
.cal-head .next{position:absolute;right:28px}
.cal-grid{position:absolute;left:14px;top:58px;width:237px;display:grid;grid-template-columns:repeat(7,1fr);row-gap:5px;text-align:center}
.cal-grid span{height:20px;line-height:20px}
.cal-grid .today{border:1px solid #fff;background:#fff;color:var(--brand);width:20px;margin:0 auto}

/* packages */
.packages{position:absolute;left:0;top:991px;width:1200px;height:611px;background:var(--band)}
.packages h2{position:absolute;left:0;top:22px;width:1200px;text-align:center;font-size:30px;font-weight:300;color:var(--brand)}
.plan{position:absolute;top:108px;width:265px;height:455px;background:linear-gradient(180deg,#f5f8fb 0%,#f1f5f9 60%,#cfe1f0 100%);border:2px solid #fff;box-shadow:0 0 3px rgba(0,0,0,.25)}
.plan-head{height:88px;background:linear-gradient(180deg,#2b85cc,#1a63a8);color:#fff;text-align:center;padding-top:14px}
.plan-head .name{font-size:19px;font-weight:600;padding-left:38px}
.plan-head .price{font-size:22px;font-weight:700}
.plan-head sup{font-size:11px}
.badge{position:absolute;left:-8px;top:-6px;width:62px;height:62px}
.plan h4{margin:18px 0 0 30px;font-family:"Roboto Slab",Georgia,serif;font-size:19px;color:#333;letter-spacing:.5px}
.plan ul{list-style:none;margin:8px 30px 0}
.plan li{height:37px;line-height:37px;border-top:1px solid #dde3e8;font-size:14px;color:#555}
.plan .pay-name{margin-top:10px;text-align:center;font-size:21px;font-weight:700;color:#25408f}
.plan .signup{position:absolute;left:42px;bottom:20px;width:180px;height:52px;background:linear-gradient(180deg,var(--orange),var(--orange-dark));color:#fff;font-size:16px;font-weight:600;display:flex;flex-direction:column;align-items:center;justify-content:center;border-radius:2px;box-shadow:0 2px 2px rgba(0,0,0,.2);line-height:1.1}
.plan .signup small{font-size:10px;color:#333;font-weight:700}

/* testimonials */
.students{position:absolute;left:0;top:1602px;width:1200px;height:110px;background:#fff}
.students h3{position:absolute;left:143px;top:37px;font-size:16px;font-weight:700;color:#222}
.students .meet{position:absolute;left:148px;top:62px;font-size:14px;color:var(--muted)}
.students .divider{position:absolute;left:347px;top:32px;width:2px;height:48px;background:var(--accent-red)}
.student{position:absolute;top:18px;width:240px;height:70px}
.student .photo{position:absolute;left:0;top:0;width:68px;height:68px}
.student .who{position:absolute;left:85px;top:2px;width:140px;text-align:center;font-size:11px;font-weight:700;color:#222}
.student .meta{position:absolute;left:78px;top:16px;width:150px;text-align:center;font-size:11px;line-height:16px;color:var(--muted)}
.student .share{position:absolute;left:118px;top:53px;width:58px;height:17px;background:var(--brand);color:#fff;font-size:8px;display:flex;align-items:center;justify-content:center}

/* footer */
.site-footer{position:absolute;left:0;top:1712px;width:1200px;height:398px;background:var(--footer);color:#ccc}
.widget{position:absolute;top:40px}
.widget h5{font-size:13px;font-weight:700;color:#fff}
.widget h5::after{content:"";display:block;width:72px;height:2px;background:var(--accent-red);margin-top:14px}
.post{display:flex;gap:12px;margin-top:22px;height:50px}
.post:first-of-type{margin-top:18px}
.post .thumb{width:44px;height:44px;border:2px solid #fff}
.post b{display:block;font-size:14px;font-weight:400;color:#fff}
.post i{font-style:normal;font-size:11px;color:#aaa}
.field{width:204px;height:32px;background:#494949;margin-top:10px;padding:8px;font-size:13px;color:#999}
.field:first-of-type{margin-top:20px}
.field.tall{height:72px}
.btn-send{margin:10px 0 0 128px;width:76px;height:36px;background:var(--brand-bright);color:#fff;font-size:13px;font-weight:700;display:flex;align-items:center;justify-content:center}
.tweet{margin-top:16px;width:205px;font-size:11.5px;line-height:16px;color:#999}
.tweet:first-of-type{margin-top:20px}
.tweet .handle,.tweet .link{color:#fff}
.tweet .link{display:block;white-space:nowrap}
.tweet .ago{color:#777;font-size:11px}
.photo-grid{display:grid;grid-template-columns:repeat(4,44px);gap:6px;margin-top:20px}
.photo-grid div{height:44px;border:2px solid #fff}
.to-top{position:absolute;left:1155px;top:355px;width:34px;height:34px;background:#666;display:flex;align-items:center;justify-content:center}
.bottom-bar{position:absolute;left:0;top:2110px;width:1200px;height:53px;background:var(--footer-deep);color:#777;font-size:14px}
.bottom-bar .copy{position:absolute;left:143px;top:17px}
.social-links{position:absolute;right:170px;top:17px;display:flex;gap:20px;font-size:13px;color:#666}
</style>
</head>
<body>

<header class="site-header">
  <div class="logo">
    <div class="logo-square"></div>
    <div class="logo-name">QUOLT</div>
    <div class="logo-sub">Online Tuition</div>
  </div>
  <div class="top-btn" style="left:754px;width:160px">STUDENTS LOGIN</div>
  <div class="top-btn" style="left:929px;width:161px">ENROLMENT</div>
  <nav class="main-nav">
    <a class="current" style="left:415px">Home</a>
    <a style="left:479px">Tution Packages</a>
    <a style="left:618px">Weekly Tips</a>
    <a style="left:726px">Comments</a>
    <a style="left:830px">Reading</a>
    <a style="left:935px">Speaking</a>
    <a style="left:1045px">Writing</a>
  </nav>
</header>

<section class="hero" role="img" aria-label="Photo of a tutor shaking hands with a student in front of a seated class">
  <ul class="hero-features">
    <li>Online training though video classes</li>
    <li>Bulletpractise exams for reading, writing &amp; listening</li>
    <li>Bullet training for academic &amp; general modules</li>
    <li>Bullettutor assistance through email &amp; chat bullet</li>
    <li>You can take classes any where, any time bullet all these just for $99</li>
  </ul>
  <svg class="hero-arrow" style="left:21px" viewBox="0 0 42 42"><path d="M24 13l-8 8 8 8" stroke="#fff" stroke-width="3" fill="none"/></svg>
  <svg class="hero-arrow" style="left:1137px" viewBox="0 0 42 42"><path d="M18 13l8 8-8 8" stroke="#fff" stroke-width="3" fill="none"/></svg>
  <div class="hero-dots"><span></span><span></span><span></span></div>
</section>

<h1 class="welcome-title">Welcome to QUOLT Online Tuition</h1>
<p class="welcome-text">We put you first. We listen to you and help you find what you need. If you want help in passing an QUOLT test, we can help you with:</p>

<article class="intro-card" style="left:143px">
  <div class="thumb" role="img" aria-label="Photo of a student at a laptop" style="background:linear-gradient(135deg,#c9d3dc,#8a6a55)"></div>
  <h3>QUOLT Online Tuition</h3>
  <p>We put you first. We listen to you and help you find what you need.</p>
  <span class="btn-more">Read More</span>
</article>
<article class="intro-card" style="left:370px">
  <div class="thumb" role="img" aria-label="Illustration of an e-learning key with a pointing cursor" style="background:linear-gradient(135deg,#2a8fd4,#d8e6f2)"></div>
  <h3>Tutorial Packages</h3>
  <p>We put you first. We listen to you and help you find what you need.</p>
  <span class="btn-more">Read More</span>
</article>
<article class="intro-card" style="left:598px">
  <div class="thumb" role="img" aria-label="Photo of hands typing on a keyboard" style="background:linear-gradient(135deg,#e4e4e4,#6a6a6a)"></div>
  <h3>Weekly Tips and Comments</h3>
  <p>We put you first. We listen to you and help you find what you need.</p>
  <span class="btn-more">Read More</span>
</article>

<aside class="calendar">
  <span class="close">×</span>
  <div class="cal-head"><span class="prev">◂</span>JANUARY • 2014<span class="next">▸</span></div>
  <div class="cal-grid">
    <span>MON</span><span>TUE</span><span>WED</span><span>THU</span><span>FRI</span><span>SUT</span><span>SUN</span>
    <span>1</span><span>2</span><span>3</span><span>4</span><span>5</span><span>6</span><span>7</span>
    <span>8</span><span>9</span><span>10</span><span>11</span><span>12</span><span>13</span><span>14</span>
    <span>15</span><span class="today">16</span><span>17</span><span>18</span><span>19</span><span>20</span><span>21</span>
    <span>22</span><span>23</span><span>24</span><span>25</span><span>26</span><span>27</span><span>28</span>
    <span>29</span><span>30</span><span>31</span><span>1</span><span>2</span><span>3</span><span>4</span>
  </div>
</aside>

<section class="packages">
  <h2>Different packages of online tuition and payvora</h2>

  <div class="plan" style="left:162px">
    <svg class="badge" viewBox="0 0 62 62"><path d="M31 2l7 8 10-3 2 10 10 3-4 10 5 8-9 5 0 10-10-1-5 9-8-6-8 6-5-9-10 1 0-10-9-5 5-8-4-10 10-3 2-10 10 3z" fill="var(--gold)"/><text x="31" y="29" text-anchor="middle" font-size="9" font-weight="700" fill="#c0392b" transform="rotate(-20 31 31)">BEST</text><text x="31" y="39" text-anchor="middle" font-size="9" font-weight="700" fill="#c0392b" transform="rotate(-20 31 31)">VALUE!</text></svg>
    <div class="plan-head"><div class="name">Weekly Classes</div><div class="price">$49.<sup>00</sup></div></div>
    <h4>FEATURES</h4>
    <ul><li>Amazing Good Looks</li><li>Handsome Hazel Eyes</li><li>Loves to Cook</li><li>Gives Great Massages</li><li>Overall Happy Dude</li></ul>
    <div class="pay-name">payvora</div>
    <div class="signup">SIGN UP NOW</div>
  </div>

  <div class="plan" style="left:485px">
    <svg class="badge" viewBox="0 0 62 62"><path d="M31 2l7 8 10-3 2 10 10 3-4 10 5 8-9 5 0 10-10-1-5 9-8-6-8 6-5-9-10 1 0-10-9-5 5-8-4-10 10-3 2-10 10 3z" fill="var(--gold)"/><text x="31" y="29" text-anchor="middle" font-size="9" font-weight="700" fill="#c0392b" transform="rotate(-20 31 31)">BEST</text><text x="31" y="39" text-anchor="middle" font-size="9" font-weight="700" fill="#c0392b" transform="rotate(-20 31 31)">VALUE!</text></svg>
    <div class="plan-head"><div class="name">Monthly Classes</div><div class="price">$89.<sup>00</sup></div></div>
    <h4>FEATURES</h4>
    <ul><li>Amazing Good Looks</li><li>Handsome Hazel Eyes</li><li>Loves to Cook</li><li>Gives Great Massages</li><li>Overall Happy Dude</li></ul>
    <div class="pay-name">payvora</div>
    <div class="signup">SIGN UP NOW</div>
  </div>

  <div class="plan" style="left:808px">
    <svg class="badge" viewBox="0 0 62 62"><path d="M31 2l7 8 10-3 2 10 10 3-4 10 5 8-9 5 0 10-10-1-5 9-8-6-8 6-5-9-10 1 0-10-9-5 5-8-4-10 10-3 2-10 10 3z" fill="var(--gold)"/><text x="31" y="29" text-anchor="middle" font-size="9" font-weight="700" fill="#c0392b" transform="rotate(-20 31 31)">BEST</text><text x="31" y="39" text-anchor="middle" font-size="9" font-weight="700" fill="#c0392b" transform="rotate(-20 31 31)">VALUE!</text></svg>
    <div class="plan-head"><div class="name">Daily Classes</div><div class="price">$215.<sup>00</sup></div></div>
    <h4>FEATURES</h4>
    <ul><li>Amazing Good Looks</li><li>Handsome Hazel Eyes</li><li>Loves to Cook</li><li>Gives Great Massages</li><li>Overall Happy Dude</li></ul>
    <div class="pay-name">payvora</div>
    <div class="signup">SIGN UP NOW<small>CREDIT CARD OR PAYVORA</small></div>
  </div>
</section>

<section class="students">
  <h3>WHAT STUDENTS SAY</h3>
  <div class="meet">Meet to Our Students</div>
  <div class="divider"></div>
  <div class="student" style="left:370px">
    <div class="photo" role="img" aria-label="Student portrait" style="background:linear-gradient(135deg,#6b6b6b,#c9b8a8)"></div>
    <div class="who">KENJI, JAPAN</div>
    <div class="meta">QUOLT student | Result<br>| Band 7.5</div>
    <div class="share">friendwall</div>
  </div>
  <div class="student" style="left:628px">
    <div class="photo" role="img" aria-label="Student portrait" style="background:linear-gradient(135deg,#f1ece4,#4a3a2c)"></div>
    <div class="who">IRINA, RUSSIA</div>
    <div class="meta">QUOLT student | Result<br>| Band 7.5</div>
    <div class="share">friendwall</div>
  </div>
  <div class="student" style="left:880px">
    <div class="photo" role="img" aria-label="Student portrait" style="background:linear-gradient(135deg,#e3ddd5,#6e5a4a)"></div>
    <div class="who">LUCA, ITALY</div>
    <div class="meta">QUOLT student | Result<br>| Band 7.5</div>
    <div class="share">friendwall</div>
  </div>
</section>

<footer class="site-footer">
  <div class="widget" style="left:147px">
    <h5>RECENT POSTS WIDGET</h5>
    <div class="post"><div class="thumb" role="img" aria-label="Post thumbnail" style="background:#c8a890"></div><div><b>This is a Standard post</b><i>June 24, 2013</i></div></div>
    <div class="post"><div class="thumb" role="img" aria-label="Post thumbnail" style="background:#b45a4a"></div><div><b>Awesome Slider Post</b><i>May 30, 2013</i></div></div>
    <div class="post"><div class="thumb" role="img" aria-label="Post thumbnail" style="background:#d6b8a0"></div><div><b>Another Gallery post</b><i>May 1, 2013</i></div></div>
    <div class="post"><div class="thumb" role="img" aria-label="Post thumbnail" style="background:#7d6f68"></div><div><b>This is an Audio post</b><i>April 17, 2013</i></div></div>
  </div>

  <div class="widget" style="left:381px">
    <h5>CONTACT FORM</h5>
    <div class="field">Your name*</div>
    <div class="field">Your email*</div>
    <div class="field tall">Your message*</div>
    <div class="btn-send">SEND</div>
  </div>

  <div class="widget" style="left:615px">
    <h5>CHIRPLO WIDGET</h5>
    <div class="tweet"><span class="handle">@velunathemes</span> Fennick &amp;#8211; Blog Magazine &amp;#038; Review Theme <span class="link">quenmar.example/product/fenn</span><span class="ago">39 days ago</span></div>
    <div class="tweet"><span class="handle">@velunathemes</span> Iron harbour <span class="link">quenmar.example/iron-harbo</span><span class="ago">44 days ago</span></div>
    <div class="tweet"><span class="handle">@velunathemes</span> Grid <span class="link">quenmar.example/grid-2/</span><span class="ago">44 days ago</span></div>
  </div>

  <div class="widget" style="left:850px">
    <h5>SNAPBOARD WIDGET</h5>
    <div class="photo-grid">
      <div role="img" aria-label="Sunset photo" style="background:linear-gradient(#3a2a2a,#d0602a)"></div>
      <div role="img" aria-label="Gallery photo" style="background:#8a7a5a"></div>
      <div role="img" aria-label="Gallery photo" style="background:#5a7aa0"></div>
      <div role="img" aria-label="Gallery photo" style="background:#8aa0c0"></div>
      <div role="img" aria-label="Gallery photo" style="background:#6a6a6a"></div>
      <div role="img" aria-label="Gallery photo" style="background:#7a8aa0"></div>
      <div role="img" aria-label="Gallery photo" style="background:#4a4a4a"></div>
      <div role="img" aria-label="Gallery photo" style="background:#a05050"></div>
    </div>
  </div>

  <div class="to-top"><svg width="14" height="10" viewBox="0 0 14 10"><path d="M1 9l6-7 6 7" stroke="#fff" stroke-width="2.5" fill="none"/></svg></div>
</footer>

<div class="bottom-bar">
  <span class="copy">www.lingvarotutors.example @ 2014 All Rights Reserved</span>
  <div class="social-links"><span>friendwall</span><span>chirplo</span><span>talqo</span></div>
</div>

</body>
</html>
```